Letterhead for New Orthopaedic Surgery Practice

My husband and I are starting our own practice named RB Spine & Vitality Center. We would like to create a nice simple but high class letterhead that doesn't use too much solid color ink when printing. I like the colors dark blue, gold, yellow. Open to other suggestions. We will need to list him and I both on the top of the letterhead. Here is the important information:
Lucinda Perrow, M.D. - Hand and Upper Extremity Surgery
Abena Quist, M.D. - Hip & Knee Replacement/General Orthopaedic Surgery
Location: 18735 North Harlow Pkwy
Palm Crest, FL 33499
Phone: 954-218-4650
Fax: 954-582-1346
Email: info@myrbspine.com

The only thing is that the phone and fax numbers will change once we get into our space. I just want to get the design started. I am including several documents which are my previous practice letterhead, my current procedure room letterhead, and our new Logo. The other letterheads are just for examples but please think outside of the box! We would love to see some great designs.

Colors
0054AA
0677BA
7BADD7
CADEEF
E8F1F8
0094D4
00A9DD
6FCCEA
C7EBF8
E9F6FB

Requirements
Must have
• class, elegance, luxury

```html
<!DOCTYPE html>
<html lang="en">
<head>
<meta charset="utf-8">
<title>RB Spine &amp; Vitality Center – Stationery</title>
<link rel="stylesheet" href="https://fonts.googleapis.com/css2?family=Noto+Serif:wght@400;700&family=Open+Sans:wght@400&family=Roboto:wght@400&display=swap">
<style>
:root{
  --navy:#1a2a52;
  --gold:#c6a05a;
  --paper:#ffffff;
  --ink:#4a4a4a;
  --bg:#dcdde0;
}
*{box-sizing:border-box;margin:0;padding:0}
html,body{width:1200px;height:858px;overflow:hidden;background:var(--bg)}
.canvas{position:relative;width:1200px;height:858px}

/* Letterhead */
.letterhead{position:absolute;left:92px;top:101px;width:464px;height:655px;background:var(--paper);box-shadow:0 2px 8px rgba(0,0,0,.25);overflow:hidden}
.brand{position:absolute;display:flex;align-items:center;gap:6px;font-family:"Noto Serif",serif;font-weight:700;color:var(--navy)}
.brand-dot{border-radius:50%;border:1.5px solid var(--gold);flex:none}
.letterhead .brand{left:50px;top:50px;width:140px;font-size:11px;line-height:1.25}
.letterhead .brand-dot{width:26px;height:26px}
.contact{position:absolute;left:317px;top:39px;font-family:"Roboto",sans-serif;font-size:8.4px;line-height:10.8px;color:var(--ink)}
.contact .addr{margin-bottom:3px}
.contact li{list-style:none;display:flex;align-items:center;gap:4px;line-height:12px}
.contact svg{width:8px;height:8px;fill:var(--navy)}
.letter-body{position:absolute;left:47px;top:176px;width:370px;font-family:"Open Sans",sans-serif;font-size:7.9px;line-height:10.8px;color:var(--ink);text-align:justify}
.letter-body p{margin-bottom:10.8px}
.letter-body .sign{text-align:left}
.signature{position:absolute;left:47px;top:500px;width:46px;height:45px;background:#eeeeee;border-radius:4px}
.letter-footer{position:absolute;left:0;bottom:0;width:464px;height:60px}
.letter-footer svg{position:absolute;inset:0}
.doctors{position:absolute;left:0;right:0;bottom:12px;text-align:center;font-family:"Noto Serif",serif;font-size:8.4px;line-height:10.4px;color:#fff}
.doctors b{font-weight:700}

/* Envelope back */
.envelope{position:absolute;left:578px;width:531px;background:var(--paper);box-shadow:0 2px 8px rgba(0,0,0,.25)}
.envelope-back{top:101px;height:366px;background:none;box-shadow:none}
.envelope-back .sheet{position:absolute;left:0;top:101px;width:531px;height:265px;background:var(--paper);box-shadow:0 2px 8px rgba(0,0,0,.25);overflow:hidden}
.flap{position:absolute;left:0;width:531px;height:102px}
.flap .brand{color:#fff;left:50%;top:50%;transform:translate(-50%,-50%);width:150px;font-size:11px;line-height:1.25}
.flap .brand-dot{width:26px;height:26px}
.envelope-back .sheet .brand{left:34px;top:40px;width:140px;font-size:11px;line-height:1.25}
.envelope-back .sheet .brand-dot{width:26px;height:26px}
.env-footer{position:absolute;left:0;bottom:0;width:531px;height:56px}
.env-footer svg{position:absolute;inset:0}
.env-address{position:absolute;left:0;right:0;bottom:17px;text-align:center;font-family:"Roboto",sans-serif;font-size:11.6px;color:#fff}

/* Envelope front */
.envelope-front{top:488px;height:265px}
</style>
</head>
<body>
<div class="canvas">

  <section class="letterhead">
    <div class="brand"><span class="brand-dot"></span><span>RB Spine &amp; Vitality Center</span></div>
    <div class="contact">
      <div class="addr">18735 North Harlow Pkwy<br>Palm Crest, FL 33499</div>
      <ul>
        <li><svg viewBox="0 0 10 10"><path d="M1 4C1 2 3 1 5 1s4 1 4 3H7V3H3v1zM2 5h6l1 4H1z"/></svg>954-218-4650</li>
        <li><svg viewBox="0 0 10 10"><path d="M3 1h4v2H3zM1 4h8v4H7v1H3V8H1zM3 7v1h4V7z"/></svg>954-582-1346</li>
        <li><svg viewBox="0 0 10 10"><path d="M1 2h8v1L5 6 1 3zM1 4l4 3 4-3v4H1z"/></svg>info@myrbspine.com</li>
      </ul>
    </div>
    <div class="letter-body">
      <p class="sign">Dear customer,</p>
      <p>Lorem ipsum dolor sit amet, consectetur adipisicing elit, sed do eiusmod tempor incididunt ut labore et dolore magna aliqua. Ut enim ad minim veniam, quis nostrud exercitation ullamco laboris nisi ut aliquip ex ea commodo consequat. Duis aute irure dolor in reprehenderit in voluptate velit esse cillum dolore eu fugiat nulla pariatur. Excepteur sint occaecat cupidatat non proident, sunt in culpa qui officia deserunt mollit anim id est laborum.</p>
      <p>Lorem ipsum dolor sit amet, consectetur adipisicing elit, sed do eiusmod tempor incididunt ut labore et dolore magna aliqua. Ut enim ad minim veniam, quis nostrud exercitation ullamco laboris nisi ut aliquip ex ea commodo consequat. Duis aute irure dolor in reprehenderit in voluptate velit esse cillum dolore eu fugiat nulla pariatur. Excepteur sint occaecat cupidatat non proident, sunt in culpa qui officia deserunt mollit anim id est laborum.</p>
      <p>Lorem ipsum dolor sit amet, consectetur adipisicing elit, sed do eiusmod tempor incididunt ut labore et dolore magna aliqua. Ut enim ad minim veniam, quis nostrud exercitation ullamco laboris nisi ut aliquip ex ea commodo consequat. Duis aute irure dolor in reprehenderit in voluptate velit esse cillum dolore eu fugiat nulla pariatur. Excepteur sint occaecat cupidatat non proident, sunt in culpa qui officia deserunt mollit anim id est laborum.</p>
      <p>Lorem ipsum dolor sit amet, consectetur adipisicing elit, sed do eiusmod tempor incididunt ut labore et dolore magna aliqua. Ut enim ad minim veniam, quis nostrud exercitation ullamco laboris nisi ut aliquip ex ea commodo consequat. Duis aute irure dolor in reprehenderit.</p>
      <p class="sign">Yours Sincerely,</p>
      <p class="sign" style="margin-top:16px">Marcus Hale<br>General Director</p>
    </div>
    <div class="signature" role="img" aria-label="Handwritten signature"></div>
    <footer class="letter-footer">
      <svg viewBox="0 0 464 60" preserveAspectRatio="none">
        <path d="M0 36Q210 0 464 15V60H0Z" fill="var(--navy)"/>
        <path d="M0 24Q180 -2 350 2Q180 4 0 32Z" fill="var(--gold)"/>
      </svg>
      <div class="doctors">
        <b>Lucinda Perrow, M.D.</b> - Hand and Upper Extremity Surgery<br>
        <b>Abena Quist, M.D.</b> - Hip &amp; Knee Replacement/General Orthopaedic Surgery
      </div>
    </footer>
  </section>

  <section class="envelope envelope-back">
    <svg class="flap" style="top:0" viewBox="0 0 531 102">
      <path d="M14 10Q16 0 30 0H500Q514 0 516 10L531 102H0Z" fill="var(--navy)"/>
    </svg>
    <div class="flap" style="top:0"><div class="brand"><span class="brand-dot"></span><span>RB Spine &amp; Vitality Center</span></div></div>
    <div class="sheet">
      <div class="brand"><span class="brand-dot"></span><span>RB Spine &amp; Vitality Center</span></div>
      <div class="env-footer">
        <svg viewBox="0 0 531 56" preserveAspectRatio="none">
          <path d="M0 38Q240 0 531 17V56H0Z" fill="var(--navy)"/>
          <path d="M0 25Q210 -2 400 1Q210 4 0 34Z" fill="var(--gold)"/>
        </svg>
        <div class="env-address">18735 North Harlow Pkwy Palm Crest, FL 33499</div>
      </div>
    </div>
  </section>

  <section class="envelope envelope-front">
    <svg class="flap" style="top:0" viewBox="0 0 531 102">
      <path d="M0 0H531L516 90Q514 102 500 102H30Q16 102 14 90Z" fill="var(--navy)"/>
    </svg>
    <div class="flap" style="top:0"><div class="brand"><span class="brand-dot"></span><span>RB Spine &amp; Vitality Center</span></div></div>
  </section>

</div>
</body>
</html>
```